Food Safety Consultancy Flyer Design

We need a flyer design for a new company called Tundo Training. New food safety regulations are coming into effect for all food operators in March 2016. My company provides training and resources to support food operators during the transition onto the new Food Control Plan. For the designs we would like to see any of the colours used from the logo which is attached. The flyer will be letting operators know that there are new regulations and we are here to help. Our company offers three packages: 1. Videos (training videos) 2. Webinars and Workshop 3. One-on-one mentoring. Our websites main colour used is the green colour from the logo.
Food service operators: cafes, restaurants etc.
Hospitality

```html
<!DOCTYPE html>
<html lang="en">
<head>
<meta charset="utf-8">
<title>Tundo Training – Food Act 2014 Flyer</title>
<link rel="stylesheet" href="https://fonts.googleapis.com/css2?family=Arimo:wght@700&family=Marcellus+SC&family=Open+Sans:wght@400;700&display=swap">
<style>
  :root {
    --page-bg: #ececec;
    --paper: #ffffff;
    --navy: #0d3a8c;
    --ink: #1a1a1a;
    --body-grey: #555a60;
    --heading-grey: #6b6b6b;
    --orange: #f7a21b;
    --green: #43d62a;
    --blue: #2f80f0;
    --brown: #7a4a0c;
    --tan: #f2c98b;
    --dark-green: #1f7a16;
    --light-green: #8ee57a;
    --deep-blue: #0a3d8f;
    --light-blue: #8db8f0;
    --photo-light: #f3f3f3;
    --photo-mid: #dcdcdc;
  }
  * { box-sizing: border-box; margin: 0; padding: 0; }
  html, body { width: 1200px; height: 1000px; overflow: hidden; }
  body { background: var(--page-bg); position: relative; font-family: "Open Sans", Arial, sans-serif; }

  .flyer {
    position: absolute; left: 260px; top: 20px;
    width: 680px; height: 960px;
    background: var(--paper);
    box-shadow: 0 4px 18px rgba(0,0,0,.18);
    overflow: hidden;
  }
  .brand {
    height: 150px;
    display: flex; align-items: center; justify-content: center; gap: 16px;
  }
  .brand-dot { width: 34px; height: 34px; border-radius: 50%; background: var(--orange); }
  .brand-name { font-family: "Open Sans", Arial, sans-serif; font-weight: 700; font-size: 54px; color: var(--ink); letter-spacing: 1px; }

  .photo-backdrop {
    position: absolute; left: 0; top: 150px; width: 100%; height: 730px;
    background: linear-gradient(180deg, var(--photo-mid) 0%, var(--photo-light) 45%, var(--photo-mid) 100%);
  }
  .content { position: absolute; left: 0; top: 150px; width: 100%; height: 730px; padding: 28px 40px 0; }

  .headline { color: var(--navy); font-weight: 700; font-size: 27px; line-height: 1.2; text-align: center; text-transform: uppercase; }
  .headline .date { text-transform: none; }
  .intro { color: var(--body-grey); font-size: 17px; line-height: 1.35; text-align: center; margin-top: 12px; }
  .subhead { color: var(--navy); font-weight: 700; font-size: 21px; line-height: 1.25; text-align: center; text-transform: uppercase; margin-top: 18px; }

  .topics { list-style: none; display: grid; grid-template-columns: 1.2fr 1fr; gap: 6px 20px; margin-top: 12px; padding: 0 10px; }
  .topics li { font-family: "Marcellus SC", Georgia, serif; font-size: 18px; color: var(--ink); display: flex; align-items: center; gap: 8px; }
  .topics li::before { content: ""; width: 15px; height: 15px; border-radius: 50%; flex: none; }
  .topics .orange::before { background: var(--orange); }
  .topics .green::before { background: var(--light-green); }

  .packages-title { font-family: "Arimo", Arial, sans-serif; font-weight: 700; font-size: 38px; color: var(--heading-grey); text-align: center; margin-top: 22px; }

  .packages { display: grid; grid-template-columns: repeat(3, 1fr); gap: 16px; margin-top: 18px; }
  .package { display: flex; flex-direction: column; align-items: center; text-align: center; }
  .package-badge {
    width: 168px; height: 168px; border-radius: 50%;
    display: flex; align-items: center; justify-content: center;
    border: 16px solid; color: #fff;
    font-family: "Marcellus SC", Georgia, serif; font-size: 22px; line-height: 1.15;
  }
  .package--videos .package-badge { background: var(--brown); border-color: var(--tan); font-size: 28px; }
  .package--webinars .package-badge { background: var(--dark-green); border-color: var(--light-green); }
  .package--mentoring .package-badge { background: var(--deep-blue); border-color: var(--light-blue); }
  .package-text { font-family: "Marcellus SC", Georgia, serif; font-size: 15px; line-height: 1.25; color: var(--ink); margin-top: 14px; max-width: 185px; }

  .contact {
    position: absolute; left: 0; bottom: 0; width: 100%; height: 80px; background: var(--paper);
    display: flex; align-items: center; justify-content: space-between; padding: 0 34px;
  }
  .contact-item { display: flex; align-items: center; gap: 10px; color: var(--navy); font-size: 18px; }
  .contact-item svg { width: 22px; height: 22px; flex: none; }
</style>
</head>
<body>
  <article class="flyer">
    <header class="brand">
      <span class="brand-dot"></span>
      <span class="brand-name">Tundo Training</span>
    </header>

    <div class="photo-backdrop" role="img" aria-label="Faded photograph of cutlery on a grey wooden table"></div>

    <section class="content">
      <h1 class="headline">The Food Act 2014 comes into force<br><span class="date">ON 1 March 2016</span></h1>
      <p class="intro">Food service and food retailers will be on Food Control Plans – documentation of processes and risk management to produce safe and suitable food.</p>
      <h2 class="subhead">Your reputation is our business with<br>up-to-date knowledge on:</h2>
      <ul class="topics">
        <li class="orange">Food Control Plan requirements</li>
        <li class="orange">Verification expectations</li>
        <li class="green">New Food Grading system</li>
        <li class="green">New Fees</li>
      </ul>

      <h2 class="packages-title">OUR PACKAGES</h2>
      <div class="packages">
        <div class="package package--videos">
          <div class="package-badge">Viideos</div>
          <p class="package-text">Animated training videos of the FCP 6 month subscription translated into Mandarin, Japanese, Korean and Hindi</p>
        </div>
        <div class="package package--webinars">
          <div class="package-badge">Webinars<br>Workshops</div>
          <p class="package-text">A range of webinars at times to suit the hospitality industry and half day training workshops. 6 month subscription to the video library is included</p>
        </div>
        <div class="package package--mentoring">
          <div class="package-badge">One-to-one<br>Mentoring</div>
          <p class="package-text">We come to you and go through the FCP page-by-page</p>
        </div>
      </div>
    </section>

    <footer class="contact">
      <span class="contact-item">
        <svg viewBox="0 0 24 24" aria-hidden="true"><circle cx="12" cy="12" r="11" fill="#0d3a8c"/><path d="M1 12h22M12 1c3.5 3.5 3.5 18.5 0 22M12 1c-3.5 3.5-3.5 18.5 0 22" stroke="#fff" stroke-width="1.4" fill="none"/></svg>
        www.tundotraining.co.nz
      </span>
      <span class="contact-item">
        <svg viewBox="0 0 24 24" aria-hidden="true"><rect x="1" y="4" width="22" height="16" rx="2" fill="#0d3a8c"/><path d="M3 7l9 7 9-7" stroke="#fff" stroke-width="1.6" fill="none"/></svg>
        info@tundotraining.co.nz
      </span>
    </footer>
  </article>
</body>
</html>
```